I need a business Card Design for my practice , i am clinical herbalist. I am a herbalist specializing in Lyme disease, autism, autoimmune diseases, difficult to cure diseasesDifficult to cure diseases. In my innovative practice i link traditional medicine, herbs with science, immunologu ,pharmacology.

Industry/Entity Type

Business

Contact Information for Business Card

My company name : OŚRODEK ZIELNIK
My name : Piotr Kaleta
Name of my profession : Fitoterapeuta
In Polish language Fitoterapeuta is Herbalist .

e-mail: piotrkaleta@osrodekzielnik.com
www.osrodek-zielnik.pl
phone : 604 587 231
My company adress : Dąbrowa Sitnicka 41 , 38-415 Lużna
I dont have logo .

Requirements
Nice to have
• My company

```html
<!DOCTYPE html>
<html lang="pl">
<head>
<meta charset="UTF-8">
<title>Business Card – Clinical Herbalist</title>
<link rel="stylesheet" href="https://fonts.googleapis.com/css2?family=Cormorant+Garamond:wght@500;600&family=Questrial&family=Open+Sans:wght@700&family=Dancing+Script:wght@600&display=swap">
<style>
  :root {
    --page-bg: #f2f2f2;
    --card-bg: #ffffff;
    --green-light: #3cb043;
    --green-mid: #1f9444;
    --green-dark: #006b35;
    --name-red: #c8102e;
    --title-blue: #1e6fc0;
    --ink: #1a1a1a;
    --white: #ffffff;
  }
  * { margin: 0; padding: 0; box-sizing: border-box; }
  html, body {
    width: 1000px;
    height: 1200px;
    overflow: hidden;
    background: var(--page-bg);
  }
  .stage {
    position: relative;
    width: 1000px;
    height: 1200px;
  }
  .card-frame {
    position: absolute;
    left: 50px;
    top: 309px;
    width: 900px;
    height: 582px;
    box-shadow: 0 10px 28px rgba(0,0,0,0.28);
    background: var(--card-bg);
    overflow: hidden;
  }
  .card {
    position: absolute;
    left: 0;
    top: 0;
    width: 490px;
    height: 317px;
    transform: scale(1.8367);
    transform-origin: top left;
  }
  .card-panel {
    position: absolute;
    left: 0;
    top: 0;
    width: 490px;
    height: 317px;
  }
  .services {
    position: absolute;
    left: 13px;
    color: var(--white);
  }
  .services--specializing { top: 84px; }
  .services--practice { top: 199px; }
  .services__heading {
    font-family: "Cormorant Garamond", serif;
    font-weight: 600;
    font-size: 12px;
    letter-spacing: 0.3px;
    margin-bottom: 17px;
  }
  .services__list {
    list-style: none;
    font-family: "Questrial", sans-serif;
    font-size: 9px;
    word-spacing: 2px;
  }
  .services__list li {
    line-height: 14.3px;
  }
  .services__list li::before {
    content: "";
    display: inline-block;
    width: 3px;
    height: 3px;
    border-radius: 50%;
    background: var(--white);
    margin: 0 4px 1px 1px;
    vertical-align: middle;
  }
  .identity {
    position: absolute;
    left: 255px;
    top: 124px;
  }
  .identity__name {
    font-family: "Open Sans", sans-serif;
    font-weight: 700;
    font-size: 22px;
    color: var(--name-red);
    letter-spacing: -0.2px;
    line-height: 25px;
    white-space: nowrap;
  }
  .identity__title {
    font-family: "Dancing Script", cursive;
    font-weight: 600;
    font-size: 19px;
    color: var(--title-blue);
    line-height: 19px;
    margin-left: 15px;
    white-space: nowrap;
  }
  .identity__emblem {
    position: absolute;
    left: 404px;
    top: 142px;
    width: 28px;
    height: 28px;
  }
  .contact {
    position: absolute;
    left: 388px;
    top: 293px;
    display: flex;
    align-items: center;
    gap: 2px;
  }
  .contact__icon {
    width: 21px;
    height: 21px;
  }
  .contact__phone {
    font-family: "Questrial", sans-serif;
    font-size: 11.5px;
    color: var(--ink);
    letter-spacing: 0.2px;
  }
</style>
</head>
<body>
<main class="stage">
  <div class="card-frame">
    <article class="card">
      <svg class="card-panel" viewBox="0 0 490 317" aria-hidden="true">
        <defs>
          <linearGradient id="panel-gradient" x1="0" y1="0" x2="1" y2="0.6">
            <stop offset="0" stop-color="var(--green-mid)"/>
            <stop offset="1" stop-color="var(--green-dark)"/>
          </linearGradient>
        </defs>
        <path class="panel-edge" d="M0,0 L74,0 L287,262 Q296,282 272,298 L232,317 L0,317 Z" fill="var(--green-light)"/>
        <path class="panel-fill" d="M0,0 L66,0 L277,262 Q285,280 260,295 L218,317 L0,317 Z" fill="url(#panel-gradient)"/>
      </svg>

      <section class="services services--specializing">
        <h2 class="services__heading">Specializing</h2>
        <ul class="services__list">
          <li>Autism</li>
          <li>Lyme Disease</li>
          <li>Difficult to Cure Diseases</li>
          <li>Autoimmune Diseases</li>
        </ul>
      </section>

      <section class="services services--practice">
        <h2 class="services__heading">Innovative Practice</h2>
        <ul class="services__list">
          <li>Traditional Medicine</li>
          <li>Herbs with Science</li>
          <li>Immunology</li>
          <li>Pharmacology</li>
        </ul>
      </section>

      <header class="identity">
        <h1 class="identity__name">NAME IS HERE</h1>
        <p class="identity__title">Clinical Herbalist</p>
      </header>

      <svg class="identity__emblem" viewBox="0 0 28 28" role="img" aria-label="Placeholder for herbal mortar emblem">
        <circle cx="14" cy="14" r="14" fill="var(--green-light)"/>
      </svg>

      <div class="contact">
        <svg class="contact__icon" viewBox="0 0 20 20" aria-hidden="true">
          <circle cx="10" cy="10" r="10" fill="var(--green-light)"/>
          <path d="M7.2,5 L8.8,5 L9.4,7.8 L8.3,8.6 Q9.2,10.9 11.4,11.8 L12.2,10.7 L15,11.3 L15,12.9 Q14.6,14.8 12.4,14.6 Q6.2,13.6 5.4,7.4 Q5.3,5.3 7.2,5 Z" fill="var(--white)"/>
        </svg>
        <span class="contact__phone">xxx-xxx-xxx</span>
      </div>
    </article>
  </div>
</main>
</body>
</html>
```